" Hoje temos o nome fantasia de NÚCLEO APRENDER PLENO VIRTUAL, mas somos mais conhecidos na cidade pela marca que a gente trabalha (VELMIRA). Estamos no mercado de Educação à Distância em Goianésia e região há 18 anos com a melhor Graduação e Pós-Graduação na modalidade EAD. E já com 7 anos consecutivos reconhecida por pesquisa de opinião pública, a melhor da região. Somos únicos na modalidade de aula semipresencial com tutores capacitados e graduados nos respectivos cursos, dando suporte ao nosso aluno. Única instituição EAD em fazer acontecer a colação de grau nos mesmos moldes do ensino presencial. Temos também o único EJA da cidade na modalidade a distancia, autorizado pelo Câmara Provincial de Ensino, que possibilita pessoas terminarem seu ensino médio em, no máximo, um ano e meio. Como novidade estamos trabalhando com educação de tecnologia, educação financeira e comunicação para crianças e adolescentes. "

```html
<!DOCTYPE html>
<html lang="pt-BR">
<head>
<meta charset="utf-8">
<title>Papel Timbrado – Avante Educacional</title>
<link href="https://fonts.googleapis.com/css2?family=Montserrat:wght@400;500;600;700&display=swap" rel="stylesheet">
<style>
  :root {
    --bg: #e9ebee;
    --paper: #ffffff;
    --navy: #22375f;
    --blue: #1d9bd7;
    --blue-light: #5cc3ef;
    --text: #55606e;
    --mark: #f2f3f5;
  }
  * { margin: 0; padding: 0; box-sizing: border-box; }
  html, body {
    width: 1200px; height: 1200px; overflow: hidden;
    background: var(--bg);
    font-family: "Montserrat", sans-serif;
  }
  .canvas {
    position: relative; width: 1200px; height: 1200px;
    display: flex; align-items: center; justify-content: center;
  }
  .letterhead {
    position: relative; width: 780px; height: 1104px;
    background: var(--paper);
    box-shadow: 0 10px 30px rgba(0,0,0,0.12);
    overflow: hidden;
  }
  .brand {
    position: absolute; left: 66px; top: 46px;
    display: flex; align-items: center; gap: 14px;
  }
  .brand-dot {
    width: 46px; height: 46px; border-radius: 50%;
    background: var(--blue);
  }
  .brand-name {
    font-weight: 700; font-size: 24px; line-height: 1.05;
    color: var(--navy); letter-spacing: 0.5px;
  }
  .brand-name span { display: block; font-size: 12.5px; letter-spacing: 4.6px; }
  .website {
    position: absolute; right: 66px; top: 70px;
    font-size: 15px; font-weight: 500; color: var(--text); letter-spacing: 0.3px;
  }
  .backdrop-mark {
    position: absolute; left: 50%; top: 51%;
    width: 460px; height: 460px; margin: -230px 0 0 -230px;
    border-radius: 50%; background: var(--mark);
  }
  .footer {
    position: absolute; left: 0; right: 0; bottom: 42px;
    display: flex; flex-direction: column; align-items: center; gap: 10px;
    font-size: 11.5px; color: var(--text);
  }
  .footer-row { display: flex; gap: 34px; align-items: center; }
  .contact { display: flex; align-items: center; gap: 7px; }
  .contact svg { width: 17px; height: 17px; flex: none; }
  .social { display: flex; gap: 4px; }
  .social i { width: 15px; height: 15px; border-radius: 50%; background: var(--blue); display: block; }
  .address { line-height: 1.3; }
  .footer-bar {
    position: absolute; left: 150px; right: 150px; bottom: 28px; height: 6px;
    background: linear-gradient(90deg, var(--blue), var(--blue-light));
    border-radius: 3px;
  }
</style>
</head>
<body>
<div class="canvas">
  <div class="letterhead">
    <header class="brand">
      <div class="brand-dot"></div>
      <div class="brand-name">AVANTE<span>EDUCACIONAL</span></div>
    </header>
    <div class="website">www.avanteeduca.net</div>

    <div class="backdrop-mark"></div>

    <footer class="footer">
      <div class="footer-row">
        <div class="contact">
          <svg viewBox="0 0 20 20"><circle cx="10" cy="10" r="10" fill="#1d9bd7"/><path d="M7 5.5l1.6 0 .8 2.4-1.1.9a6 6 0 0 0 2.9 2.9l.9-1.1 2.4.8v1.6c0 .6-.5 1-1.1 1A8 8 0 0 1 6 6.6c0-.6.4-1.1 1-1.1z" fill="#fff"/></svg>
          (99) 4815-7206
        </div>
        <div class="contact">
          <svg viewBox="0 0 20 20"><circle cx="10" cy="10" r="10" fill="#1d9bd7"/><rect x="5" y="6.5" width="10" height="7" rx="1" fill="#fff"/><path d="M5.3 7l4.7 3.6L14.7 7" stroke="#1d9bd7" stroke-width="1" fill="none"/></svg>
          atendimento@avanteeduca.net
        </div>
      </div>
      <div class="footer-row">
        <div class="contact">
          <svg viewBox="0 0 20 20"><circle cx="10" cy="10" r="10" fill="#1d9bd7"/><path d="M10 4.5a3.6 3.6 0 0 0-3.6 3.6c0 2.7 3.6 7 3.6 7s3.6-4.3 3.6-7A3.6 3.6 0 0 0 10 4.5z" fill="#fff"/><circle cx="10" cy="8.1" r="1.3" fill="#1d9bd7"/></svg>
          <div class="address">Rua 18, nº 512 - Bairro Aurora<br>Vila Serena - Planalto Sul - CEP 00.418-090</div>
        </div>
        <div class="contact">
          <div class="social"><i></i><i></i></div>
          @avanteeduca
        </div>
      </div>
    </footer>
    <div class="footer-bar"></div>
  </div>
</div>
</body>
</html>
```